Web Design Project

Psychotherapist in Private Practice
Practice name "The Quiet Harbour"
The population is professional adults seeking life coaching and change consultation
I am including a photo for inspiration ONLY - It includes the theme of light and tree branches. There does not HAVE to be a photograph . An illustration , concept or theme of nature /light / generativity / growth / creativity is acceptable
Clean sharp lines Light colors, minimalist , modern.
There is a separate project for a logo design that will become part of the web design
Here are examples of two logos/websites I like
http://www.brightmeadowcentre.ca/
http://www.openridgeadvisors.ca/

Target Market(s)

Professional adults seeking life coaching

Industry/Entity Type

Life Coaching

Requirements
Should not have
• Although the business name has 'compassion' in it, designs with hearts in it would have to be pretty stylish, subtle, mature and sophisticated to be considered.

```html
<!DOCTYPE html>
<html lang="en">
<head>
<meta charset="utf-8">
<title>The Quiet Harbour</title>
<link rel="stylesheet" href="https://fonts.googleapis.com/css2?family=Mulish:wght@300;400;600;700&display=swap">
<style>
:root{
  --wood-dark:#2a160d;
  --wood-mid:#4a2614;
  --wood-light:#6a3a20;
  --accent:#4ab8e6;
  --button:#6dcdf5;
  --green:#a5d23c;
  --paper:#f8f7f3;
  --rule:#e0dedb;
  --text:#4a4a4a;
  --list:#545454;
  --frame:#e8e6e4;
  --white:#ffffff;
}
*{margin:0;padding:0;box-sizing:border-box}
html,body{width:1000px;height:1200px;overflow:hidden}
body{position:relative;background:var(--paper);font-family:'Mulish',sans-serif;color:var(--text)}
.abs{position:absolute}

.header{left:0;top:0;width:1000px;height:398px;
  background:linear-gradient(90deg,var(--wood-mid),var(--wood-light) 20%,var(--wood-dark) 45%,var(--wood-light) 70%,var(--wood-mid));}
.header::before{content:"";position:absolute;inset:0;background:linear-gradient(180deg,rgba(0,0,0,.55),rgba(0,0,0,.15) 40%,rgba(0,0,0,.35));}
.top-strip{left:0;top:0;width:1000px;height:7px;background:#2b2220}
.green-band{left:0;top:398px;width:1000px;height:5px;background:var(--green)}

.brand{left:104px;top:21px;display:flex;align-items:center;gap:10px}
.brand-mark{width:48px;height:48px;border-radius:50%;background:var(--white)}
.brand-name{font-size:17px;font-weight:700;color:var(--white);text-transform:uppercase;letter-spacing:-.2px}

.main-nav a,.footer-nav a{position:absolute;text-decoration:none;font-size:13.5px;color:var(--accent);white-space:nowrap}
.main-nav a{top:37px}
.main-nav a.current,.footer-nav a.current{color:var(--white)}

.hero-frame{left:102px;top:82px;width:795px;height:292px;background:var(--frame);box-shadow:0 8px 18px rgba(0,0,0,.5)}
.hero-image{left:113px;top:92px;width:774px;height:271px;
  background:linear-gradient(180deg,#e9c66a 0%,#fbe89a 35%,#f5d27a 55%,#8a7460 72%,#6b5a55 100%)}
.hero-panel{left:582px;top:116px;width:280px;height:227px;background:rgba(80,75,70,.6);text-align:center;color:var(--white)}
.hero-title{margin-top:9px;font-size:27px;font-weight:400;line-height:36px}
.hero-title span{color:var(--button)}
.hero-copy{margin-top:11px;font-size:11px;font-weight:600;line-height:16.5px;padding:0 12px}

.btn{display:block;background:var(--button);color:var(--white);font-size:12.5px;font-weight:600;text-transform:uppercase;text-align:center;text-decoration:none;border-bottom:2px solid #3fb0e0}
.hero-btn{left:651px;top:290px;width:141px;height:35px;line-height:33px}

.section-title{left:125px;font-size:15px;font-weight:600;color:var(--accent)}
.rule{left:103px;width:795px;height:1px;background:var(--rule)}
.intro{left:126px;top:464px;width:760px;font-size:13.3px;font-weight:300;line-height:29px;letter-spacing:.3px;color:var(--text)}
.intro a{color:var(--accent);font-size:11.5px;font-weight:700;text-decoration:none;margin-left:6px}

.feature-list{list-style:none;font-size:11px;font-weight:700;color:var(--list);letter-spacing:.3px}
.feature-list li{height:33.3px;display:flex;align-items:center;gap:9px}
.feature-list svg{flex:none}

.photo{top:849px;width:250px;height:208px;background:var(--white);padding:5px;box-shadow:0 0 3px rgba(0,0,0,.12)}
.photo div{width:100%;height:100%}
.photo-dandelion{background:linear-gradient(135deg,#e6e8ec,#b8c4d4 60%,#9aaac0)}
.photo-shore{background:linear-gradient(180deg,#5a4a5e 0%,#a0706a 30%,#e3b97a 48%,#3c9a96 62%,#2a6a6a 100%)}
.photo-wheat{background:linear-gradient(160deg,#cfe1f2 0%,#e8d7a8 45%,#c8923a 75%,#a8702a 100%)}

.bottom-btn{left:429px;top:1083px;width:142px;height:36px;line-height:34px}

.footer{left:0;top:1143px;width:1000px;height:57px;border-top:2px solid #6a4a35;
  background:linear-gradient(90deg,var(--wood-mid),var(--wood-light) 30%,var(--wood-mid) 60%,var(--wood-light))}
.footer-nav a{top:19px}
.copyright{right:108px;top:19px;font-size:13.5px;color:var(--white)}
</style>
</head>
<body>
<header>
  <div class="abs header"></div>
  <div class="abs top-strip"></div>
  <div class="abs brand"><div class="brand-mark"></div><span class="brand-name">The Quiet Harbour</span></div>
  <nav class="main-nav">
    <a class="current" href="#" style="left:467px">Home</a>
    <a href="#" style="left:538px">About</a>
    <a href="#" style="left:612px">Services</a>
    <a href="#" style="left:698px">Events</a>
    <a href="#" style="left:771px">Contact</a>
    <a href="#" style="left:852px">Find Us</a>
  </nav>
  <div class="abs hero-frame"></div>
  <div class="abs hero-image" role="img" aria-label="Sunset over the sea seen beneath overhanging tree branches"></div>
  <div class="abs hero-panel">
    <h1 class="hero-title"><span>Life coaching</span> and<br><span>change consultation</span><br>for professionals</h1>
    <p class="hero-copy">Morbi quis augue venenatis, auctor orci utmo llis ipsum proin augue nisl, tempor id velit sit</p>
  </div>
  <a class="abs btn hero-btn" href="#">Contact Us</a>
  <div class="abs green-band"></div>
</header>

<main>
  <h2 class="abs section-title" style="top:424px">What we do &amp; how we can help you...</h2>
  <div class="abs rule" style="top:455px"></div>
  <p class="abs intro">Lorem ipsum dolor sit amet, consectetur adipiscing elit. In aliquet malesuada ultrices. Vivamus varius, nisl et placerat rhoncus, augue nisi lobortis nunc, sit amet sagittis tortor sem eu tellus. Cum sociis natoque penatibus et magnis dis parturient montes, nascetur ridiculus mus.<br>Dum sociis natoque penatibus et magnis dis parturient montes, nascetur ridiculus musullam at leo leom Integer vitae imperdiet nunc. Nulla lacus nulla, ultrices quis sem ut. <a href="#">CONTACT US &gt;</a></p>

  <h2 class="abs section-title" style="top:633px">List of features &amp; services...</h2>
  <div class="abs rule" style="top:664px"></div>

  <ul class="abs feature-list" style="left:126px;top:680px">
    <li><svg width="6" height="9" viewBox="0 0 6 9"><path d="M1 1l3.5 3.5L1 8" stroke="#8cc43c" stroke-width="2" fill="none"/></svg>Lorem ipsum dolor sit amet</li>
    <li><svg width="6" height="9" viewBox="0 0 6 9"><path d="M1 1l3.5 3.5L1 8" stroke="#8cc43c" stroke-width="2" fill="none"/></svg>Sectetur adipiscing elitn aliquet</li>
    <li><svg width="6" height="9" viewBox="0 0 6 9"><path d="M1 1l3.5 3.5L1 8" stroke="#8cc43c" stroke-width="2" fill="none"/></svg>Vivamus varius nisl et placerat</li>
    <li><svg width="6" height="9" viewBox="0 0 6 9"><path d="M1 1l3.5 3.5L1 8" stroke="#8cc43c" stroke-width="2" fill="none"/></svg>Im sociis natoque penatibus</li>
  </ul>
  <ul class="abs feature-list" style="left:402px;top:680px">
    <li><svg width="6" height="9" viewBox="0 0 6 9"><path d="M1 1l3.5 3.5L1 8" stroke="#8cc43c" stroke-width="2" fill="none"/></svg>Donec ut molestie elit.</li>
    <li><svg width="6" height="9" viewBox="0 0 6 9"><path d="M1 1l3.5 3.5L1 8" stroke="#8cc43c" stroke-width="2" fill="none"/></svg>Duis in dictum ligula id volutpat</li>
    <li><svg width="6" height="9" viewBox="0 0 6 9"><path d="M1 1l3.5 3.5L1 8" stroke="#8cc43c" stroke-width="2" fill="none"/></svg>Aliquam erat volutpat.</li>
    <li><svg width="6" height="9" viewBox="0 0 6 9"><path d="M1 1l3.5 3.5L1 8" stroke="#8cc43c" stroke-width="2" fill="none"/></svg>Curabitur vestibulum luctus mal</li>
  </ul>
  <ul class="abs feature-list" style="left:675px;top:680px">
    <li><svg width="6" height="9" viewBox="0 0 6 9"><path d="M1 1l3.5 3.5L1 8" stroke="#8cc43c" stroke-width="2" fill="none"/></svg>Lorem ipsum dolor sit amet</li>
    <li><svg width="6" height="9" viewBox="0 0 6 9"><path d="M1 1l3.5 3.5L1 8" stroke="#8cc43c" stroke-width="2" fill="none"/></svg>Sectetur adipiscing elitn aliquet</li>
    <li><svg width="6" height="9" viewBox="0 0 6 9"><path d="M1 1l3.5 3.5L1 8" stroke="#8cc43c" stroke-width="2" fill="none"/></svg>Vivamus varius nisl et placerat</li>
    <li><svg width="6" height="9" viewBox="0 0 6 9"><path d="M1 1l3.5 3.5L1 8" stroke="#8cc43c" stroke-width="2" fill="none"/></svg>Im sociis natoque penatibus</li>
  </ul>

  <figure class="abs photo" style="left:104px"><div class="photo-dandelion" role="img" aria-label="Dandelion seeds drifting against a soft grey sky"></div></figure>
  <figure class="abs photo" style="left:375px"><div class="photo-shore" role="img" aria-label="Sunset over a calm turquoise sea with rocks on the shore"></div></figure>
  <figure class="abs photo" style="left:646px"><div class="photo-wheat" role="img" aria-label="Golden ears of wheat against a pale blue sky"></div></figure>

  <a class="abs btn bottom-btn" href="#">Contact Us</a>
</main>

<footer>
  <div class="abs footer"></div>
  <nav class="footer-nav">
    <a class="current" href="#" style="left:105px;top:1162px">Home</a>
    <a href="#" style="left:176px;top:1162px">About</a>
    <a href="#" style="left:250px;top:1162px">Services</a>
    <a href="#" style="left:335px;top:1162px">Events</a>
    <a href="#" style="left:408px;top:1162px">Contact</a>
    <a href="#" style="left:490px;top:1162px">Find Us</a>
  </nav>
  <p class="abs copyright" style="top:1162px">© 2013 Company Name</p>
</footer>
</body>
</html>
```